Mossy Pail Mercantile Farm-to-Table Restaurant Menu

We are a farm-to-table restaurant. We grow all of our natural raised and finished grass-fed beef. No hormones or antibiotics ever. We try and source many of our products locally as well. We also sell Kansas products and our meats and Kansas cheeses and butters in our restaurant. It's almost like a Tin Lantern setting. Our restaurant is on main street in an old drug store from the 1920s. It features an old-soda fountain so we make all of our drinks and shakes, malts by hand. I need help re-designing my menu plus I want to add some items.
I would like one side to be the breakfast menu and the other side to be the lunch and supper menu. I would also like to create a separate drink/dessert menu.
I need to add some more items as well.

Target Market(s)

Farmers, Cowboys, Rural community less than 1200 people in town, regenerative & sustainability conscience

Industry/Entity Type

Ag

Font styles to use
Sans Serif

Colors
0054AA
0677BA
7BADD7
CADEEF
E8F1F8
0094D4
00A9DD
6FCCEA
C7EBF8
E9F6FB
00AB8E
00BBA5
67D7C9
C6EFE9
E9F9F6
FFF300
FFF600
FEFA6F
FFFEC7
FFFEE8
FFC000
F8CF3A
FAE287
FDF2CF
FEFAEE
EB3D1F
EC4F4E
F09395
F8D3D4
FCEDEE

Requirements
Must have
• Clean lines-easy to read prices-help with food descriptions
Nice to have
• Like to incorporate some of our story if there is room.

```html
<!DOCTYPE html>
<html lang="en">
<head>
<meta charset="utf-8">
<title>Mossy Pail Mercantile – Lunch &amp; Supper Menu</title>
<link href="https://fonts.googleapis.com/css2?family=Bowlby+One+SC&family=Encode+Sans+Condensed:wght@400;600;700&family=Open+Sans:wght@700;800&display=swap" rel="stylesheet">
<style>
  :root {
    --backdrop: #9a9a9a;
    --ink: #0b0b0b;
    --paper: #ffffff;
    --teal: #a6d7d4;
    --teal-deep: #8ccbc7;
    --red: #d3131a;
    --text-light: #ffffff;
    --text-soft: #e9e9e9;
    --text-dark: #1a1a1a;
    --photo-warm: #8a5a3c;
    --photo-cool: #3d6fb0;
  }
  * { box-sizing: border-box; margin: 0; padding: 0; }
  html, body { width: 1200px; height: 1177px; overflow: hidden; background: var(--backdrop); }
  .menu {
    position: absolute; left: 223px; top: 84px; width: 781px; height: 1010px;
    overflow: hidden; font-family: "Encode Sans Condensed", "Arial Narrow", sans-serif;
  }
  .menu-backdrop { position: absolute; inset: 0; }

  .brand-badge {
    position: absolute; left: 567px; top: 12px; width: 164px; height: 164px; border-radius: 50%;
    background: var(--teal); border: 5px solid var(--ink);
    display: flex; align-items: center; justify-content: center; text-align: center;
  }
  .brand-name {
    font-family: "Encode Sans Condensed", sans-serif; font-weight: 700; font-size: 22px;
    line-height: 1.1; color: var(--ink); text-transform: uppercase; letter-spacing: 1px;
  }

  .food-photo {
    position: absolute; top: 194px; width: 148px; height: 148px; border-radius: 50%;
    border: 5px dotted var(--paper); padding: 5px;
  }
  .food-photo span { display: block; width: 100%; height: 100%; border-radius: 50%; border: 4px solid var(--teal); }
  .food-photo--left { left: 430px; }
  .food-photo--left span { background: radial-gradient(circle at 40% 40%, var(--photo-warm), #4a2f22 60%, var(--photo-cool)); }
  .food-photo--right { left: 583px; }
  .food-photo--right span { background: radial-gradient(circle at 50% 45%, #a07a45, #5c3e26 60%, var(--photo-cool)); }

  .section-banner {
    position: absolute; left: 43px; top: 122px; width: 336px; height: 64px;
    background: var(--teal); text-align: center; padding-top: 6px;
  }
  .section-banner h2 {
    font-family: "Bowlby One SC", sans-serif; font-weight: 400; font-size: 25px;
    color: var(--ink); letter-spacing: 1px; line-height: 1.1;
  }
  .section-banner p { font-family: "Open Sans", sans-serif; font-weight: 700; font-size: 15px; color: var(--ink); line-height: 1.1; }

  .item { position: absolute; width: 350px; color: var(--text-light); }
  .item--left { left: 43px; }
  .item--right { left: 417px; width: 323px; }
  .item-name { font-family: "Open Sans", sans-serif; font-weight: 800; font-size: 15.5px; line-height: 1.15; width: 270px; }
  .item-price { position: absolute; right: 0; top: 0; font-family: "Open Sans", sans-serif; font-weight: 800; font-size: 15.5px; }
  .item-desc { font-size: 12.5px; line-height: 1.25; color: var(--text-soft); width: 285px; margin-top: 1px; }
  .item-note { position: absolute; left: 43px; top: 730px; font-size: 12.5px; color: var(--text-soft); }

  .plates {
    position: absolute; left: 404px; top: 500px; width: 352px; height: 300px; background: var(--red);
  }
  .plates-title {
    position: absolute; left: 16px; top: 17px; width: 322px; height: 47px;
    background: var(--paper); border: 3px solid var(--ink); outline: 2px solid var(--paper);
    display: flex; align-items: center; justify-content: center;
    font-family: "Bowlby One SC", sans-serif; font-size: 22px; color: var(--ink); letter-spacing: 1px;
  }
  .plates .item { left: 18px; width: 320px; }

  .appetizers {
    position: absolute; left: 40px; top: 811px; width: 716px; height: 142px; background: var(--teal);
  }
  .appetizers h2 {
    position: absolute; left: 17px; top: 12px;
    font-family: "Bowlby One SC", sans-serif; font-weight: 400; font-size: 22px; color: var(--red); letter-spacing: 1px;
  }
  .appetizer-list {
    position: absolute; left: 17px; top: 50px; list-style: none;
    font-family: "Open Sans", sans-serif; font-weight: 700; font-size: 12.4px; line-height: 17.6px; color: var(--text-dark);
  }
  .sep { color: var(--red); }

  .kids {
    position: absolute; left: 428px; top: 15px; width: 272px; height: 110px;
    background: var(--paper); border: 2px solid var(--red); outline: 2px solid var(--paper); padding: 6px 12px;
  }
  .kids h3 { font-family: "Bowlby One SC", sans-serif; font-weight: 400; font-size: 16px; color: var(--red); line-height: 1.2; }
  .kids h3 small { font-size: 10px; }
  .kids ul { list-style: none; margin-top: 4px; }
  .kids li {
    display: flex; justify-content: space-between;
    font-family: "Open Sans", sans-serif; font-weight: 700; font-size: 12px; line-height: 16px; color: var(--text-dark);
  }

  .contact-bar {
    position: absolute; left: 36px; top: 967px; width: 720px; height: 60px;
    background: var(--paper); border-radius: 12px 12px 0 0;
    display: flex; justify-content: center; padding-top: 12px; gap: 10px;
    font-family: "Open Sans", sans-serif; font-weight: 800; font-size: 15.5px;
  }
  .contact-bar .address, .contact-bar .phone { color: var(--red); }
  .contact-bar .web { color: var(--ink); }
  .contact-bar .divider { color: #b5b5b5; font-weight: 400; }
</style>
</head>
<body>
<main class="menu">
  <svg class="menu-backdrop" viewBox="0 0 781 1010" width="781" height="1010" aria-hidden="true">
    <rect width="781" height="1010" fill="var(--paper)"/>
    <path d="M0 80 C150 32 320 22 470 48 L470 220 L0 220 Z" fill="var(--teal)"/>
    <path d="M380 46 C520 58 640 112 781 98 L781 220 L380 220 Z" fill="var(--red)"/>
    <path d="M0 100 C150 52 320 40 450 62 C560 82 660 132 781 132 L781 1010 L0 1010 Z" fill="var(--ink)"/>
  </svg>

  <div class="brand-badge"><span class="brand-name">Mossy Pail<br>Mercantile</span></div>

  <div class="food-photo food-photo--left" role="img" aria-label="Photo of a plated sandwich on a checkered paper liner"><span></span></div>
  <div class="food-photo food-photo--right" role="img" aria-label="Photo of steak fries topped with jalapeños"><span></span></div>

  <header class="section-banner">
    <h2>Sandwiches &amp; More</h2>
    <p>includes choice of side</p>
  </header>

  <div class="item item--left" style="top:200px">
    <p class="item-name">The Mossy Pail Chicken Fry</p><span class="item-price">12.75</span>
    <p class="item-desc">Mossy Pail beef patty served on a brioche bun with your choice of toppings.</p>
  </div>
  <div class="item item--left" style="top:256px">
    <p class="item-name">The Philly</p><span class="item-price">12.75</span>
    <p class="item-desc">Mossy Pail beef patty served on a brioche bun with your choice of toppings.</p>
  </div>
  <div class="item item--left" style="top:311px">
    <p class="item-name">Monte Cristo</p><span class="item-price">11.50</span>
    <p class="item-desc">Three pieces of ham layered with two pieces of swiss fried between two pieces of french toast topped with powdered sugar served with raspberry jam on the side.</p>
  </div>
  <div class="item item--left" style="top:383px">
    <p class="item-name">Grilled Sandwich Melt</p><span class="item-price">9.50</span>
    <p class="item-desc">Choose between sliced roast beef, ham, or turkey piled with your choice of cheese grilled to perfection.</p>
  </div>
  <div class="item item--left" style="top:438px">
    <p class="item-name">Mossy Pail Club Sandwich</p><span class="item-price">10.25</span>
    <p class="item-desc">Bacon, ham, and turkey stacked between pieces of jalapeno jack cheese, lettuce, and tomato on three pieces of Texas Toast.</p>
  </div>
  <div class="item item--left" style="top:511px">
    <p class="item-name">Mossy Pail Ranch Steak Fries</p><span class="item-price">12.25</span>
    <p class="item-desc">Mossy Pail steak served on a bed of hand cut fries topped with cheddar cheese and a side of Mossy Pail sauce.</p>
  </div>
  <div class="item item--left" style="top:577px">
    <p class="item-name">Mossy Pail Steak &amp; Bacon<br>Mac 'n Cheese</p><span class="item-price">13.75</span>
    <p class="item-desc">Mossy Pail steak and bacon served on top of home made mac 'n cheese topped with cheddar cheese and side of Ranch.</p>
  </div>
  <div class="item item--left" style="top:662px">
    <p class="item-name">Buffalo Chicken Mac 'n Cheese</p><span class="item-price">11.50</span>
    <p class="item-desc">Mossy Pail all-natural lightly hand breaded chicken sliced on a warm pile of homemade mac 'n cheese topped with buffalo sauce and ranch dressing.</p>
  </div>
  <p class="item-note">Make it a Wrap</p>
  <div class="item item--left" style="top:744px">
    <p class="item-name">It's Not Beef</p><span class="item-price">12.25</span>
    <p class="item-desc">A Mossy Pail fried or grilled chicken breast topped with your choice of cheese served on a brioche bun.</p>
  </div>

  <div class="item item--right" style="top:379px">
    <p class="item-name">Jalapeno Popper Grilled Cheese</p><span class="item-price">9.50</span>
    <p class="item-desc">This hot sandwich features Kansas cheeses layered with jalapenos grilled to perfection on Texas Toast.</p>
  </div>
  <div class="item item--right" style="top:434px">
    <p class="item-name">Grilled Bacon Mac 'n Cheese</p><span class="item-price">9.75</span>
    <p class="item-desc">Homemade mac 'n cheese layered with bacon grilled between two pieces of Texas Toast.</p>
  </div>

  <section class="plates">
    <h2 class="plates-title">Mossy Pail Plates</h2>
    <div class="item" style="top:86px">
      <p class="item-name">Chicken Fried Steak</p><span class="item-price">13.85</span>
      <p class="item-desc">Mossy Pail hand breaded chicken fried steak served with homemade clumpy mashed potatoes with country gravy and a side salad.</p>
    </div>
    <div class="item" style="top:158px">
      <p class="item-name">Chicken Fried Chicken</p><span class="item-price">13.25</span>
      <p class="item-desc">Mossy Pail hand breaded white chicken breast served with homemade clumpy mashed potatoes with country gravy and a side salad.</p>
    </div>
    <div class="item" style="top:228px">
      <p class="item-name">Mossy Pail Hamburger Steak</p><span class="item-price">12.50</span>
      <p class="item-desc">A MP ground beef patty topped with your choice of white or brown gravy served with mashed potatoes.</p>
    </div>
  </section>

  <section class="appetizers">
    <h2>Appetizers</h2>
    <ul class="appetizer-list">
      <li>Deep Fried Cheese Curds $ 7.50 <span class="sep">|</span> Fried Mushrooms: $8.50 <span class="sep">|</span></li>
      <li>Mossy Pail Cheese Fries $8.50 <span class="sep">|</span> Fried Pickle Slices: $7.50 <span class="sep">|</span></li>
      <li>Mossy Pail Jalapeno Poppers: $6.50 <span class="sep">|</span></li>
      <li>Loaded Nachos -Choose Steak or Chicken $12.50 <span class="sep">|</span></li>
      <li>Mossy Pail Chicken Wings: $9.75 Buffalo, BBQ, Lemon Pepper</li>
    </ul>
    <div class="kids">
      <h3>Kiddie lunch <small>(Includes one side)</small></h3>
      <ul>
        <li><span>Grilled Cheese</span><span>5.25</span></li>
        <li><span>PB &amp; J</span><span>4.50</span></li>
        <li><span>Hamburger</span><span>6.50</span></li>
        <li><span>Cheeseburger</span><span>7.25</span></li>
        <li><span>Grilled Steak or Chicken Bites</span><span>8.50</span></li>
      </ul>
    </div>
  </section>

  <footer class="contact-bar">
    <span class="address">408 N. ELM ST., HARLAN, KS 67000</span>
    <span class="divider">|</span>
    <span class="phone">(620) 555-0148</span>
    <span class="divider">|</span>
    <span class="web">MOSSYPAILMERCANTILE.COM</span>
  </footer>
</main>
</body>
</html>
```